An internal sign in a physiotherapy clinic with gym. About working hard

We are a physiotherapy clinic / gym and we are wanting an internal wall to be a large sign with a great slogan
We are after 3 parts to it
1. The image / backdrop
2. The slogan
3. Our clinic logo

I have attached some images of the concept of what we are after. It can be climbing a mountain, rockclimbing and even hard work in a gym.

The slogan is:
"IF IT DOESN'T CHALLENGE YOU, IT WON'T CHANGE YOU"

Logo
I have attached a few different versions of our logo to assist you in the sign based on the background

THE SIGN SIZE WILL BE:
2935mm wide x 1885mm high

```html
<!DOCTYPE html>
<html lang="en">
<head>
<meta charset="utf-8">
<title>Challenge Wall Sign</title>
<link rel="stylesheet" href="https://fonts.googleapis.com/css2?family=Barlow+Condensed:ital,wght@0,600;1,500;1,800&family=Barlow:wght@400&display=swap">
<style>
  :root {
    --stage: #6b6b6b;
    --navy: #141a4a;
    --cyan: #4cc6ec;
    --yellow: #f5e03a;
    --sky-top: #f4f3ef;
    --sky-mid: #ece2d6;
    --sky-low: #c9b3a6;
    --rock-dark: #2a1a12;
    --rock-mid: #5a3a28;
    --ink: #111111;
  }
  html, body {
    margin: 0;
    padding: 0;
    width: 800px;
    height: 1200px;
    overflow: hidden;
    background: var(--stage);
  }
  .sign {
    position: absolute;
    left: 40px;
    top: 369px;
    width: 720px;
    height: 462px;
    display: block;
  }
  .brand-name { font-family: "Barlow Condensed", sans-serif; font-weight: 600; }
  .brand-sub { font-family: "Barlow", sans-serif; font-weight: 400; letter-spacing: 4px; }
  .slogan-lead, .slogan-tail { font-family: "Barlow Condensed", sans-serif; font-style: italic; font-weight: 500; }
  .slogan-key { font-family: "Barlow Condensed", sans-serif; font-style: italic; font-weight: 800; }
</style>
</head>
<body>
<svg class="sign" viewBox="0 0 720 462" xmlns="http://www.w3.org/2000/svg" aria-label="Wall sign: If it doesn't challenge you, it won't change you">
  <defs>
    <linearGradient id="sky" x1="0" y1="0" x2="0" y2="1">
      <stop offset="0" stop-color="var(--sky-top)"/>
      <stop offset="0.6" stop-color="var(--sky-mid)"/>
      <stop offset="1" stop-color="var(--sky-low)"/>
    </linearGradient>
    <linearGradient id="rock" x1="1" y1="0" x2="0" y2="0.6">
      <stop offset="0" stop-color="var(--rock-dark)"/>
      <stop offset="0.55" stop-color="var(--rock-mid)" stop-opacity="0.85"/>
      <stop offset="1" stop-color="var(--rock-mid)" stop-opacity="0"/>
    </linearGradient>
    <linearGradient id="climber" x1="0" y1="0" x2="0" y2="1">
      <stop offset="0" stop-color="var(--rock-dark)" stop-opacity="0.55"/>
      <stop offset="1" stop-color="var(--rock-dark)" stop-opacity="0.15"/>
    </linearGradient>
  </defs>

  <rect class="backdrop-sky" width="720" height="462" fill="url(#sky)" role="img" aria-label="Hazy evening sky backdrop"/>
  <rect class="backdrop-cliff" x="350" y="0" width="370" height="300" fill="url(#rock)" role="img" aria-label="Overhanging rock cliff"/>
  <rect class="backdrop-climber" x="330" y="55" width="200" height="250" rx="20" fill="url(#climber)" role="img" aria-label="Silhouette of a rock climber on a rope"/>

  <g class="accents">
    <polygon class="accent-band" points="0,325 0,338 170,462 188,462" fill="var(--cyan)" opacity="0.5"/>
    <polygon class="accent-dots" points="10,360 70,360 185,462 90,462" fill="var(--navy)" opacity="0.35" role="img" aria-label="Halftone dot pattern"/>
    <circle class="accent-ring" cx="26" cy="293" r="17" fill="#ffffff" fill-opacity="0.35" stroke="var(--yellow)" stroke-width="3"/>
    <path class="accent-plus" d="M157 358h12M163 352v12" stroke="var(--navy)" stroke-width="2"/>
    <polygon class="accent-triangle" points="652,310 678,312 662,332" fill="none" stroke="var(--navy)" stroke-width="2.5" opacity="0.75"/>
    <g class="accent-chevrons">
      <polygon points="213,330 231,316 249,330 249,342 231,328 213,342" fill="var(--cyan)"/>
      <polygon points="213,353 231,339 249,353 249,365 231,351 213,365" fill="var(--navy)"/>
      <polygon points="213,376 231,362 249,376 249,388 231,374 213,388" fill="var(--cyan)"/>
    </g>
  </g>

  <g class="brand">
    <circle class="brand-mark" cx="60" cy="78" r="14" fill="var(--cyan)"/>
    <text class="brand-name" x="84" y="86" font-size="30" fill="var(--navy)">KESTREL</text>
    <text class="brand-sub" x="85" y="102" font-size="10" fill="var(--cyan)">SPORTS MEDICINE</text>
  </g>

  <g class="slogan">
    <text class="slogan-lead" x="56" y="179" font-size="64" fill="var(--navy)" textLength="234" lengthAdjust="spacingAndGlyphs">IF IT DOESN'T</text>
    <text class="slogan-key" x="42" y="287" font-size="132" fill="var(--navy)" textLength="576" lengthAdjust="spacingAndGlyphs">CHALLENGE</text>
    <text class="slogan-key" x="280" y="397" font-size="132" fill="var(--navy)" textLength="186" lengthAdjust="spacingAndGlyphs">YOU</text>
    <text class="slogan-tail" x="482" y="360" font-size="44" fill="var(--ink)" textLength="108" lengthAdjust="spacingAndGlyphs">IT WON'T</text>
    <text class="slogan-tail" x="478" y="398" font-size="44" fill="var(--ink)" textLength="164" lengthAdjust="spacingAndGlyphs">CHANGE YOU</text>
  </g>
</svg>
</body>
</html>
```